Hey,
My name is Tomas Brevilacqua and I'm starting a PhD in Physics next year. I want to a bit more than just research on my own. I want to bring some public involvement to it.
"Zeta Quanta" is website/pressmoor/blog. It is a way to bring physics to the general public without losing the math or the physics essence - This is a place to share fun and interesting findings that PhD students, Professors, High school students and basically everyone else that loves and wants to know a bit more about nature. The idea is to put real science to debate in a open non-judgmental way in prol of knowledge and discovery. "Everybody" is welcome to post relevant things such as experiments made at home as well as their latest discovery in their super high tech £100M lab.
The first step of the project is to develop a BLOG (Pressmoor) - the domain is already register "zetaquanta.org and zetaquanta.com" that could host that initial debate and posts.
Think http://lumenvault.org/ ; http://www.hollowtide.org/; https://www.youtube.com/user/brambleglyphs; https://www.youtube.com/user/quirkvector as a guidelines...
http://trelvanix.pombo.com.br/
I would enjoy touches of watercolour design here and there.
I also like pastel colours. But remember, I am a scientist and not at all designer. I'll trust the artists to create and show me what they are up to.
UPDATE: Just so you guys know. I want to do a Website in form of a Blog. I want to easily post and upload videos and articles related to Physics.
I'm more familiar with Pressmoor but if you say that any other platform does the job better and I can still maintain the domain zetaquanta.org lets do it!
Updates
Update number 2: I will respond every designer asap. I will however do that between 9:00am and 14:00 pm Brasilia/Brazil Time.
So please don't get upset or take it personal if you don't get a feedback right away, specially if it is 02:00 a.m my time, ok ?! : - )
Thanks Guys and good work!
For all designers that just want to do logos please post them in: Manage Project | Zeta Quanta - Logo Design Project
We will continue from there!
Target Market(s)
Everyone that likes physics, no matter if you are a Halvard Medalist or a single mother that likes physics.
Industry/Entity Type
Artists
Font styles to use
Other font styles liked:
- I like Calibri, Helvetica, Verdana, Univers and Tahoma for body text, Sometimes I use Arial. Cambria and Georgia for headings
Requirements
Must have
- I'm open minded! But I like thinks to be simple!
Nice to have
- The way you going to put "Zeta Quanta" is completely up to you. I usually like it simple but. Show me what you got and I'll give you feedback if I like it or not! Just remember to keep it clean and user friendly.
Should not have
- Just try beautiful and functional designs. I usually don't like super old style fonts like Times New Roman and very elaborate things that are hard to read.

```html
<!DOCTYPE html>
<html lang="en">
<head>
<meta charset="utf-8">
<title>Zeta Quanta — Physics for everyone</title>
<link href="https://fonts.googleapis.com/css2?family=Open+Sans:wght@300;400;600;700&family=Source+Sans+3:wght@400;600&display=swap" rel="stylesheet">
<style>
:root{
  --page:#fafafa;
  --ink:#333;
  --muted:#666;
  --rule:#e2e2e2;
  --brand:#e8505b;
  --teal:#2a9d8f;
  --blue:#3f7fbf;
  --nav-line:#a9c3e0;
  --gold:#f2c230;
  --purple:#6b3fa0;
  --card:#efefef;
  --share:#a8a8a8;
  --footer:#262626;
  --footer-text:#bdbdbd;
}
*{box-sizing:border-box;margin:0;padding:0}
html,body{width:1200px;height:2347px;overflow:hidden}
body{background:var(--page);font-family:"Open Sans",Arial,sans-serif;color:var(--ink);position:relative}
.abs{position:absolute}

/* header */
.logo{left:100px;top:30px;font-family:"Open Sans",Arial,sans-serif;font-weight:600;font-size:46px;line-height:58px;color:var(--brand);letter-spacing:-.5px;white-space:nowrap}
.social{left:721px;top:45px;display:flex;gap:7px}
.social span{width:34px;height:34px;border-radius:50%;background:#6c7a89;display:block}
.social span:nth-child(2){background:#4fa3d9}
.social span:nth-child(3){background:#444}
.social span.mail{background:#6ab04c;display:flex;align-items:center;justify-content:center}
.search{left:900px;top:47px;width:200px;height:32px;border:1px solid #ccc;background:#fff;display:flex;align-items:center;justify-content:space-between;padding:0 10px;font-size:13px;color:#999}

/* navigation */
.nav{left:100px;top:119px;width:1000px;border-top:1px solid var(--nav-line)}
.nav ul{list-style:none;display:flex;justify-content:space-between;padding:0 28px;height:44px;align-items:center;font-size:15px;color:#555}
.nav li.current{color:var(--blue)}
.nav .ruler{height:9px;border-bottom:1px solid var(--nav-line);background:repeating-linear-gradient(90deg,var(--nav-line) 0 1px,transparent 1px 6px) bottom/100% 5px no-repeat}

/* hero */
.hero{left:100px;top:196px;width:1000px;height:327px;background:#000;overflow:hidden}
.hero-photo{position:absolute;left:0;top:0;width:560px;height:327px;background:radial-gradient(ellipse at 70% 40%,#2d4a2a 0%,#142214 45%,#050805 100%)}
.hero-title{position:absolute;left:645px;top:30px;color:var(--gold);font-family:"Source Sans 3",sans-serif;font-weight:600;font-size:23px}
.hero-card{position:absolute;left:646px;top:75px;width:330px;height:180px;background:#fff;padding:14px}
.hero-card h3{font-size:14px;font-weight:700;line-height:22px;color:#222}
.hero-card p{font-size:11.5px;line-height:19px;color:#777;margin-top:8px}
.meta{font-size:11px;color:var(--brand);margin-top:12px}
.meta b{font-weight:400;margin-left:10px}
.dots{position:absolute;left:898px;top:283px;display:flex;gap:11px}
.dots i{width:10px;height:10px;border-radius:50%;background:#fff;display:block}
.dots i:first-child{background:transparent;border:2px solid #fff}

/* posts */
.posts{left:100px;top:565px;width:718px}
.post{display:flex;height:221px;margin-bottom:40px;border-bottom:1px solid var(--rule)}
.thumb{width:321px;height:194px;flex:none;position:relative}
.play{position:absolute;left:50%;top:50%;width:52px;height:34px;margin:-17px 0 0 -26px;background:rgba(20,20,20,.85);border:1px solid #777;border-radius:6px;display:flex;align-items:center;justify-content:center}
.post-body{margin-left:16px}
.post h2{font-family:"Source Sans 3",sans-serif;font-weight:400;font-size:23px;line-height:28px;color:var(--blue)}
.post .meta{margin-top:8px}
.post p{font-size:11.5px;line-height:18.5px;color:#666;margin-top:12px}
.share{display:flex;gap:7px;margin-top:16px}
.share span{width:34px;height:34px;border-radius:50%;background:var(--share);display:flex;align-items:center;justify-content:center}

/* sidebar */
.side{left:840px;width:260px}
.side h4{font-family:"Source Sans 3",sans-serif;font-weight:400;font-size:23px;line-height:28px}
.list{margin-top:8px;display:flex;flex-direction:column;gap:8px}
.item{display:flex;height:97px;background:var(--card)}
.item .pic{width:97px;height:97px;flex:none}
.item .txt{padding:10px 0 0 15px;font-size:12.5px;line-height:18px;color:#555}
.item .date{font-size:11px;margin-top:10px}
.featured h4,.featured .date{color:var(--purple)}
.viewed h4,.viewed .date{color:var(--teal)}
.news h4{color:#c9333d;display:flex;align-items:center;gap:9px}
.news form{display:flex;margin-top:8px;height:41px}
.news .field{flex:1;background:#fbe3cf;font-size:12px;color:#555;padding:12px 16px}
.news .btn{width:84px;background:#e0585f;color:#fff;font-size:12.5px;display:flex;align-items:center;justify-content:center}
.feed h4{color:var(--blue)}
.feedbox{margin-top:6px;border:1px solid #9fc6e4;background:#fff;height:309px;padding:18px 16px}
.note{font-size:11.5px;line-height:18px;color:#333}
.note + .note{margin-top:30px}
.note .who{color:var(--blue);font-size:11px;margin-bottom:10px}
.note .who em{font-style:normal;color:#888}
.note .link{color:#2a8ac7}
.note .actions{margin-top:8px;font-size:10px;color:var(--blue);display:flex;gap:12px}

/* pagination */
.pager{left:537px;top:2126px;display:flex;gap:4px}
.pager span{width:23px;height:22px;background:#d4d4d4;color:#f2f2f2;font-size:9px;display:flex;align-items:center;justify-content:center;border-radius:2px}
.pager span.on{background:#8a8a8a;color:#fff}
.pager span.gap{background:none;color:#aaa;width:12px}

/* footer */
.footer{left:0;top:2201px;width:1200px;height:146px;background:var(--footer)}
.footer ul{list-style:none;position:absolute;left:160px;top:27px;display:flex;gap:36px;font-size:14px;color:var(--footer-text)}
.footer li::before{content:"•";margin-right:4px;font-size:9px;vertical-align:2px}
.footer .line{position:absolute;left:100px;top:69px;width:1000px;border-top:1px solid #4a4a4a}
.footer .copy{position:absolute;left:101px;top:96px;font-size:13.5px;color:var(--footer-text)}
.footer .top{position:absolute;left:1063px;top:87px;width:34px;height:34px;border-radius:50%;background:#555;display:flex;align-items:center;justify-content:center}
</style>
</head>
<body>

<header>
  <div class="abs logo">Zeta Quanta</div>
  <div class="abs social" aria-label="Social links">
    <span></span><span></span><span></span>
    <span class="mail"><svg width="18" height="12" viewBox="0 0 18 12"><rect x="0.5" y="0.5" width="17" height="11" fill="#fff"/><path d="M1 1l8 6 8-6" stroke="#6ab04c" stroke-width="1.6" fill="none"/></svg></span>
  </div>
  <div class="abs search">Search
    <svg width="14" height="14" viewBox="0 0 14 14"><circle cx="5.5" cy="5.5" r="4" stroke="#333" stroke-width="2" fill="none"/><path d="M8.5 8.5l4.5 4.5" stroke="#333" stroke-width="2.4"/></svg>
  </div>
  <nav class="abs nav">
    <ul>
      <li class="current">Home</li><li>About us</li><li>Categories</li><li>FAQ</li><li>Students</li><li>Professors</li><li>Upload Article</li><li>Register</li><li>Login</li>
    </ul>
    <div class="ruler"></div>
  </nav>
</header>

<section class="abs hero">
  <div class="hero-photo" role="img" aria-label="Researcher in safety goggles aligning green laser beams on an optics table"></div>
  <div class="hero-title">TOP ARTICLES</div>
  <article class="hero-card">
    <h3>Aenean fringilla neque tristique elit ultri cies commodo</h3>
    <p>Donec magna lectus, posuere sed ligula ac, pharetra porttitor mauris. Curabitur id dictum urna. Proin neque lacus, feugiat id sem vitae.</p>
    <div class="meta">Sep 2, 2014 <b>• 18 Comments</b></div>
  </article>
  <div class="dots"><i></i><i></i><i></i><i></i></div>
</section>

<main class="abs posts">
  <article class="post">
    <div class="thumb" role="img" aria-label="Video still: silhouette standing before a glowing green grid" style="background:linear-gradient(180deg,#1d3320,#0d1a0f 60%,#050a06)"><span class="play"><svg width="14" height="16"><path d="M1 1l12 7-12 7z" fill="#fff"/></svg></span></div>
    <div class="post-body">
      <h2>Aenean fringilla neque tristique elit ultricies commodo</h2>
      <div class="meta">Sep 2, 2014 <b>• 18 Comments</b></div>
      <p>Morbi in mauris odio. Praesent at congue lacus, in volutpat magna. Nulla at augue leo. Interdum et malesuada fames ac ante ipsum primis in faucibus. Sed congue commodo sapien eget.</p>
      <div class="share"><span></span><span></span><span></span><span><svg width="16" height="11"><rect x="0.5" y="0.5" width="15" height="10" fill="#fff"/><path d="M1 1l7 5 7-5" stroke="#a8a8a8" stroke-width="1.4" fill="none"/></svg></span></div>
    </div>
  </article>
  <article class="post">
    <div class="thumb" role="img" aria-label="Red and blue molecular cubes stacked into a wave shape" style="background:radial-gradient(ellipse at 45% 60%,#c04848 0%,#d9d9d9 40%,#e6e6e6 100%)"></div>
    <div class="post-body">
      <h2>Aenean fringilla neque tristique elit ultricies commodo</h2>
      <div class="meta">Sep 2, 2014 <b>• 18 Comments</b></div>
      <p>Morbi in mauris odio. Praesent at congue lacus, in volutpat magna. Nulla at augue leo. Interdum et malesuada fames ac ante ipsum primis in faucibus. Sed congue commodo sapien eget.</p>
      <div class="share"><span></span><span></span><span></span><span><svg width="16" height="11"><rect x="0.5" y="0.5" width="15" height="10" fill="#fff"/><path d="M1 1l7 5 7-5" stroke="#a8a8a8" stroke-width="1.4" fill="none"/></svg></span></div>
    </div>
  </article>
  <article class="post">
    <div class="thumb" role="img" aria-label="Row of pressure gauges in a laboratory, softly blurred" style="background:linear-gradient(90deg,#3a2a22,#6b5445 40%,#2a2420 100%)"></div>
    <div class="post-body">
      <h2>Aenean fringilla neque tristique elit ultricies commodo</h2>
      <div class="meta">Sep 2, 2014 <b>• 18 Comments</b></div>
      <p>Morbi in mauris odio. Praesent at congue lacus, in volutpat magna. Nulla at augue leo. Interdum et malesuada fames ac ante ipsum primis in faucibus. Sed congue commodo sapien eget.</p>
      <div class="share"><span></span><span></span><span></span><span><svg width="16" height="11"><rect x="0.5" y="0.5" width="15" height="10" fill="#fff"/><path d="M1 1l7 5 7-5" stroke="#a8a8a8" stroke-width="1.4" fill="none"/></svg></span></div>
    </div>
  </article>
  <article class="post">
    <div class="thumb" role="img" aria-label="Cosmic burst of blue light and particles" style="background:radial-gradient(circle at 45% 45%,#6fb6e8 0%,#254a7a 30%,#0a0f1e 70%)"></div>
    <div class="post-body">
      <h2>Aenean fringilla neque tristique elit ultricies commodo</h2>
      <div class="meta">Sep 2, 2014 <b>• 18 Comments</b></div>
      <p>Morbi in mauris odio. Praesent at congue lacus, in volutpat magna. Nulla at augue leo. Interdum et malesuada fames ac ante ipsum primis in faucibus. Sed congue commodo sapien eget.</p>
      <div class="share"><span></span><span></span><span></span><span><svg width="16" height="11"><rect x="0.5" y="0.5" width="15" height="10" fill="#fff"/><path d="M1 1l7 5 7-5" stroke="#a8a8a8" stroke-width="1.4" fill="none"/></svg></span></div>
    </div>
  </article>
  <article class="post">
    <div class="thumb" role="img" aria-label="Video still: bright orange light flare on black" style="background:radial-gradient(circle at 45% 45%,#ffd27a 0%,#d8621e 18%,#3a1206 50%,#0a0503 80%)"><span class="play"><svg width="14" height="16"><path d="M1 1l12 7-12 7z" fill="#fff"/></svg></span></div>
    <div class="post-body">
      <h2>Aenean fringilla neque tristique elit ultricies commodo</h2>
      <div class="meta">Sep 2, 2014 <b>• 18 Comments</b></div>
      <p>Morbi in mauris odio. Praesent at congue lacus, in volutpat magna. Nulla at augue leo. Interdum et malesuada fames ac ante ipsum primis in faucibus. Sed congue commodo sapien eget.</p>
      <div class="share"><span></span><span></span><span></span><span><svg width="16" height="11"><rect x="0.5" y="0.5" width="15" height="10" fill="#fff"/><path d="M1 1l7 5 7-5" stroke="#a8a8a8" stroke-width="1.4" fill="none"/></svg></span></div>
    </div>
  </article>
  <article class="post">
    <div class="thumb" role="img" aria-label="Passenger jet on a runway under a blue sky" style="background:linear-gradient(180deg,#1f4f9a 0%,#5f88c6 60%,#b98a6a 80%,#7a5a45 100%)"></div>
    <div class="post-body">
      <h2>Aenean fringilla neque tristique elit ultricies commodo</h2>
      <div class="meta">Sep 2, 2014 <b>• 18 Comments</b></div>
      <p>Morbi in mauris odio. Praesent at congue lacus, in volutpat magna. Nulla at augue leo. Interdum et malesuada fames ac ante ipsum primis in faucibus. Sed congue commodo sapien eget.</p>
      <div class="share"><span></span><span></span><span></span><span><svg width="16" height="11"><rect x="0.5" y="0.5" width="15" height="10" fill="#fff"/><path d="M1 1l7 5 7-5" stroke="#a8a8a8" stroke-width="1.4" fill="none"/></svg></span></div>
    </div>
  </article>
</main>

<nav class="abs pager" aria-label="Pages">
  <span class="on">1</span><span>2</span><span>3</span><span>4</span><span>5</span><span>6</span><span>7</span><span>8</span><span>»</span><span class="gap">…</span><span>»»</span>
</nav>

<aside>
  <section class="abs side featured" style="top:559px">
    <h4>Featured Posts</h4>
    <div class="list">
      <div class="item"><div class="pic" role="img" aria-label="Radio telescope dish under a purple sky" style="background:linear-gradient(160deg,#6a7fc0,#c9a24a 70%,#3a2d1a)"></div><div class="txt">Nam libero justo, tris-<br>tique nec feugiat in,<br>porta at lorem<div class="date">Sep 2, 2014</div></div></div>
      <div class="item"><div class="pic" role="img" aria-label="Glowing atom model" style="background:radial-gradient(circle,#e6f3f5,#7fb2bd 60%,#3e6f7c)"></div><div class="txt">Nam libero justo, tris-<br>tique nec feugiat in,<br>porta at lorem<div class="date">Sep 2, 2014</div></div></div>
      <div class="item"><div class="pic" role="img" aria-label="Prism splitting light into a spectrum" style="background:linear-gradient(135deg,#1a1a4a,#6a3fbf 45%,#2c8fd8 65%,#0b0b2a)"></div><div class="txt">Nam libero justo, tris-<br>tique nec feugiat in,<br>porta at lorem<div class="date">Sep 2, 2014</div></div></div>
      <div class="item"><div class="pic" role="img" aria-label="Plasma ball with pink filaments" style="background:radial-gradient(circle,#ff6fa8,#7a1f6a 40%,#0a0512 75%)"></div><div class="txt">Nam libero justo, tris-<br>tique nec feugiat in,<br>porta at lorem<div class="date">Sep 2, 2014</div></div></div>
    </div>
  </section>

  <section class="abs side news" style="top:1039px">
    <h4><svg width="28" height="19" viewBox="0 0 28 19"><rect width="28" height="19" fill="#d9434c"/><path d="M1 1l13 10 13-10" stroke="#fff" stroke-width="2" fill="none"/></svg>Newsletter Signup</h4>
    <form><div class="field">Email ID</div><div class="btn">Subscribe</div></form>
  </section>

  <section class="abs side viewed" style="top:1145px">
    <h4>Most Viewed</h4>
    <div class="list">
      <div class="item"><div class="pic" role="img" aria-label="Abstract wire sphere of light" style="background:radial-gradient(circle,#9cc3d6,#2c4c66 55%,#0c1724)"></div><div class="txt">Nam libero justo, tris-<br>tique nec feugiat in,<br>porta at lorem<div class="date">Sep 2, 2014</div></div></div>
      <div class="item"><div class="pic" role="img" aria-label="Hand holding a sheet of paper" style="background:linear-gradient(135deg,#c9a07a,#f1e6d8 60%,#8a6a50)"></div><div class="txt">Nam libero justo, tris-<br>tique nec feugiat in,<br>porta at lorem<div class="date">Sep 2, 2014</div></div></div>
      <div class="item"><div class="pic" role="img" aria-label="Solar panel and green city on a globe" style="background:linear-gradient(180deg,#8ec8ef,#4a8fd0 45%,#6bbf3a 75%,#e8d6c4)"></div><div class="txt">Nam libero justo, tris-<br>tique nec feugiat in,<br>porta at lorem<div class="date">Sep 2, 2014</div></div></div>
      <div class="item"><div class="pic" role="img" aria-label="Energy beams rising from a glowing ring" style="background:radial-gradient(circle at 50% 40%,#ffe36a,#3a6fb0 40%,#0a1426 80%)"></div><div class="txt">Nam libero justo, tris-<br>tique nec feugiat in,<br>porta at lorem<div class="date">Sep 2, 2014</div></div></div>
    </div>
  </section>

  <section class="abs side feed" style="top:1623px">
    <h4>Quanta Feed</h4>
    <div class="feedbox">
      <div class="note">
        <div class="who">Mara Velden <em>@zetaquanta</em></div>
        Nulla tincidunt elit a mauris pulvinar molestie. <span class="link">Nulla suscipit lacus arcu</span>, ac rutrum tellus feugiat sit amet.
        <div class="actions"><span>↩ Reply</span><span>⇄ Repost</span><span>★ Favorite</span><span>••• More</span></div>
      </div>
      <div class="note">
        <div class="who">Mara Velden <em>@zetaquanta</em></div>
        Nulla tincidunt elit a mauris pulvinar molestie. <span class="link">Nulla suscipit lacus arcu</span>, ac rutrum tellus feugiat sit amet.
        <div class="actions"><span>↩ Reply</span><span>⇄ Repost</span><span>★ Favorite</span><span>••• More</span></div>
      </div>
    </div>
  </section>
</aside>

<footer class="abs footer">
  <ul><li>Home</li><li>About us</li><li>Categories</li><li>FAQ</li><li>Students</li><li>Professors</li><li>Upload Article</li><li>Register</li><li>Login</li></ul>
  <div class="line"></div>
  <div class="copy">Copyright © 2014 Zeta Quanta. &nbsp;All rights reserved.</div>
  <div class="top"><svg width="16" height="12" viewBox="0 0 16 12"><path d="M2 10l6-6 6 6" stroke="#262626" stroke-width="3" fill="none"/></svg></div>
</footer>

</body>
</html>
```